Brenway Productions photography and video creator

I need a business card for my production company. I shoot photography and videography for real estate, adventure sports and businesses

simple not to busy

Colors

Designer to choose colors to be used in the design.

Requirements
Must have
• dara@brenwayproductions.ca
• phone -5803317264
• instagram dara_brenway

```html
<!DOCTYPE html>
<html lang="en">
<head>
<meta charset="utf-8">
<title>Brenway Productions – Business Card</title>
<link href="https://fonts.googleapis.com/css2?family=Public+Sans:wght@400;600&display=swap" rel="stylesheet">
<style>
  :root {
    --backdrop: #e6e0d8;
    --card: #211e1b;
    --card-edge: #2d2926;
    --ink: #cbbb9f;
    --ink-soft: #b9aa90;
    --sky-light: #c9d4da;
    --ridge-mid: #6f757a;
    --ridge-dark: #1b1a19;
  }
  * { margin: 0; padding: 0; box-sizing: border-box; }
  html, body {
    width: 1200px;
    height: 943px;
    overflow: hidden;
    background: var(--backdrop);
    font-family: "Public Sans", Arial, sans-serif;
  }
  .business-card {
    position: absolute;
    left: 398px;
    top: 85px;
    width: 426px;
    height: 748px;
    border-radius: 30px;
    background: var(--card);
    border: 2px solid var(--card-edge);
    color: var(--ink);
  }
  .brand-emblem {
    position: absolute;
    left: 52px;
    top: 80px;
    width: 318px;
    height: 318px;
    border-radius: 50%;
    background: linear-gradient(180deg, var(--sky-light) 0%, var(--ridge-mid) 40%, var(--ridge-dark) 78%);
  }
  .brand-name {
    position: absolute;
    left: 0;
    right: 0;
    top: 187px;
    text-align: center;
    font-weight: 600;
    color: var(--ink);
    line-height: 1;
  }
  .brand-name .word-main {
    display: block;
    font-size: 44px;
    letter-spacing: 1px;
  }
  .brand-name .word-sub {
    display: block;
    margin-top: 10px;
    font-size: 12px;
    letter-spacing: 6px;
  }
  .person-name {
    position: absolute;
    left: 56px;
    top: 461px;
    font-size: 30px;
    font-weight: 600;
    letter-spacing: 0.5px;
  }
  .person-role {
    position: absolute;
    left: 56px;
    top: 510px;
    font-size: 19px;
    font-weight: 400;
    color: var(--ink-soft);
  }
  .contact-list {
    position: absolute;
    left: 56px;
    top: 578px;
    list-style: none;
  }
  .contact-list li {
    display: flex;
    align-items: center;
    height: 32px;
    font-size: 19.5px;
    font-weight: 400;
  }
  .contact-icon {
    width: 17px;
    height: 17px;
    margin-right: 9px;
    flex: none;
  }
</style>
</head>
<body>
  <div class="business-card">
    <div class="brand-emblem" role="img" aria-label="Mountain landscape illustration with evergreen trees in grey tones">
      <div class="brand-name">
        <span class="word-main">BRENWAY</span>
        <span class="word-sub">PRODUCTIONS</span>
      </div>
    </div>

    <div class="person-name">DARA WHITLOW</div>
    <div class="person-role">Photograper</div>

    <ul class="contact-list">
      <li>
        <svg class="contact-icon" viewBox="0 0 24 24" aria-hidden="true">
          <path fill="var(--ink)" d="M6.6 10.8a15.1 15.1 0 0 0 6.6 6.6l2.2-2.2a1 1 0 0 1 1-.25 11.4 11.4 0 0 0 3.6.57 1 1 0 0 1 1 1V20a1 1 0 0 1-1 1A17 17 0 0 1 3 4a1 1 0 0 1 1-1h3.5a1 1 0 0 1 1 1c0 1.25.2 2.45.57 3.57a1 1 0 0 1-.25 1z"/>
        </svg>
        5803317264
      </li>
      <li>
        <svg class="contact-icon" viewBox="0 0 24 24" aria-hidden="true">
          <circle cx="12" cy="12" r="9" fill="none" stroke="var(--ink)" stroke-width="2.2"/>
        </svg>
        dara_brenway
      </li>
      <li>
        <svg class="contact-icon" viewBox="0 0 24 24" aria-hidden="true">
          <rect x="2" y="5" width="20" height="14" rx="1.5" fill="var(--ink)"/>
          <path d="M3 6l9 7 9-7" fill="none" stroke="var(--card)" stroke-width="1.8"/>
        </svg>
        dara@brenwayproductions.ca
      </li>
    </ul>
  </div>
</body>
</html>
```